pelikorax.gr wordpress makeover

We need a makeover of our wordpress website pelikorax.gr We are a company that provides astrology services via phone either by billable phone number or by prepaid packages.This is what we sell. Moreover, we share everyday astrology related articles to our blog. It will be a multy page website. Our goal is always to sell our phone prepaid packages or to make the visitor of the website call our billable numbers. Our website should have:
-a home page introducing its content (astrologers, call packages, blog section with categories).
-astrologers page (you can see the existing one to understand)
-Phone packages page (eshop page where you can buy prepaid phone packages. woo commerce maybe)
- Blog page divined by categories.
The website should have places for display banners eg. a sidebar.
I will provide some screen shots of websites we like. You can always visit our existing website www.pelikorax.gr to see it for yourself.

Target Market(s)

people seeking for future telling - astrologer services via phone. People who like to be informed about everyday astrology predictions

Industry/Entity Type

Astrology - tarot services via phone

Coding

Coded - Design and coding required

Number of Pages Required

5+ page

Font styles to use
Decorative
Script

Colors
6B429C
8869AF
B7A5CE
E3DAEB
F3F0F8

Requirements
Must have
• -Home page -Astrologers page -Phone packages page (eshop) -Blog page with categories - Made following the guidelines of google so as to be efficient in google ads marketing. Mobile friendly.
Nice to have
• Nice call to action buttons to call or buy packages. Sidebar with banner ads of maybe our offers.

```html
<!DOCTYPE html>
<html lang="el">
<head>
<meta charset="utf-8">
<title>pelikorax – Τα ζώδια για σήμερα</title>
<link rel="stylesheet" href="https://fonts.googleapis.com/css2?family=Comfortaa:wght@700&family=Open+Sans:ital,wght@0,400;0,600;0,700;1,400;1,700&display=swap">
<style>
:root{
  --violet-900:#3b1d6e;
  --violet-800:#4a2688;
  --violet-700:#5a2f98;
  --brand:#6B429C;
  --brand-mid:#8869AF;
  --brand-soft:#B7A5CE;
  --brand-pale:#E3DAEB;
  --brand-mist:#F3F0F8;
  --white:#ffffff;
  --ink:#3a3a3a;
  --heading:"Comfortaa",sans-serif;
  --body:"Open Sans",sans-serif;
}
*{box-sizing:border-box;margin:0;padding:0}
html,body{width:1200px;height:3667px;overflow:hidden}
body{font-family:var(--body);color:var(--white);background:var(--violet-800);position:relative}
.abs{position:absolute}
.bold-heading{font-family:var(--heading);font-weight:700;-webkit-text-stroke:1.1px currentColor;letter-spacing:.3px}

/* hero */
.hero{left:0;top:0;width:1200px;height:760px;background:radial-gradient(ellipse at 75% 35%,#7a3fc4 0%,#5a2a9e 40%,#4a2388 75%,#4f2b8c 100%)}
.hero-band{left:0;top:690px;width:1200px;height:140px;background:linear-gradient(rgba(120,90,190,0),rgba(120,90,190,.35) 50%,rgba(120,90,190,0))}
.site-logo{left:111px;top:40px;font-family:var(--body);font-weight:400;font-size:40px;color:var(--white);letter-spacing:.5px}
.nav a{position:absolute;top:56px;font-weight:700;font-size:16px;color:var(--white);text-decoration:none}
.call-pill{display:flex;align-items:center;gap:10px;background:var(--white);border-radius:30px;color:var(--brand);padding:4px 16px 4px 5px;text-decoration:none}
.call-pill .icon{width:34px;height:34px;border-radius:50%;border:2px solid var(--brand);display:flex;align-items:center;justify-content:center}
.call-pill small{display:block;font-size:12px;font-style:italic;font-weight:600;line-height:1}
.call-pill b{display:block;font-size:15px;line-height:1.1}
.hero-title{left:113px;top:252px;font-size:45px;line-height:69px}
.hero-lead{left:113px;top:398px;width:430px;font-style:italic;font-size:15px;line-height:23px}
.zodiac-wheel{left:572px;top:46px;width:610px;height:610px;border-radius:50%;background:radial-gradient(circle,#c9a6ff 0%,#8a55dd 30%,#6a35b8 60%,rgba(90,40,160,0) 72%);border:2px solid rgba(215,190,255,.6)}

/* astrologers */
.astrologers{left:0;top:760px;width:1200px;height:860px;background:linear-gradient(#53308f,#6a43a5 60%,#5a3596)}
.section-title{width:1200px;left:0;text-align:center;font-size:37px}
.card{background:var(--white);border-radius:4px;color:var(--ink)}
.astro-card{width:481px;height:553px;top:935px;padding:6px}
.astro-photo{width:469px;height:340px;background:linear-gradient(120deg,#2a1650,#4a2a8a 60%,#6b4fc0);position:relative}
.astro-name{position:absolute;left:270px;top:108px;color:var(--white);font-size:25px;line-height:32px}
.astro-role{position:absolute;left:270px;top:190px;border:2px solid var(--white);border-radius:22px;padding:5px 16px;color:var(--white);font-size:20px}
.contact-pill{position:absolute;top:316px;height:46px;width:185px;background:var(--white);border-radius:26px;box-shadow:0 3px 8px rgba(0,0,0,.25);display:flex;align-items:center;gap:14px;padding-left:8px;color:var(--brand);font-weight:700;font-size:31px}
.contact-pill .dot{width:36px;height:36px;border-radius:50%;background:var(--brand);display:flex;align-items:center;justify-content:center}
.astro-text{margin:46px 24px 0;font-style:italic;font-size:13px;line-height:21px;color:#444}
.astro-link{display:inline-block;margin:8px 24px;font-weight:700;font-size:16px;color:var(--brand);text-decoration:underline}
.slide-arrow{width:24px;height:24px;border-radius:50%;background:var(--white);display:flex;align-items:center;justify-content:center}

/* packages */
.packages{left:0;top:1620px;width:1200px;height:693px;background:linear-gradient(#5a3596,#4a2586 30%,#4b2787)}
.package{top:1818px;width:314px;height:342px;border:2px solid var(--white);border-radius:14px;text-align:center;padding:58px 32px 0}
.package h3{font-size:27px;line-height:39px}
.package .price{margin:10px 0 10px;font-weight:700;font-style:italic;font-size:46px}
.package p{font-style:italic;font-weight:700;font-size:13px;line-height:22px}
.package p span{font-weight:400;font-style:normal}
.package.featured{background:var(--white);color:var(--ink)}
.package.featured .price{color:var(--brand)}

/* blog */
.blog{left:0;top:2313px;width:1200px;height:960px;background:linear-gradient(#6e4bb5,#7a4cbf 45%,#8b52c6 75%,#7c3fb5)}
.post-image{background:linear-gradient(135deg,#3a1d10,#c96a2a 45%,#e8a65a)}
.post-image.globe{background:radial-gradient(circle at 45% 45%,#6fc6ff,#2a5fb0 30%,#0e1c44 70%)}
.post-card{width:410px;height:232px}
.post-rule{position:absolute;left:60px;top:0;width:2px;height:100%;background:var(--brand)}
.date{position:absolute;left:31px;top:-13px;width:59px;height:53px;background:var(--brand);color:var(--white);text-align:center;line-height:1.1;padding-top:6px}
.date small{font-size:12px;display:block}
.date b{font-size:18px}
.post-card h4{position:absolute;left:116px;top:33px;width:270px;font-family:var(--heading);font-weight:700;-webkit-text-stroke:.5px currentColor;font-size:19px;line-height:23px;color:#222}
.post-card p{position:absolute;left:116px;top:102px;width:270px;font-size:12.5px;line-height:19px;color:#555}

/* footer */
.footer{left:0;top:3273px;width:1200px;height:394px;background:linear-gradient(#7e3fb8,#8d4fb8 40%,#5a2f86 75%,#3d2260)}
.footer-logo{width:1200px;left:0;top:3352px;text-align:center;font-family:var(--body);font-weight:700;font-size:43px}
.foot-links{left:0;width:1200px;top:3420px;display:flex;justify-content:center;gap:64px;font-style:italic;font-size:17px}
.copyright{width:1200px;left:0;top:3467px;text-align:center;font-style:italic;font-size:12px}
.rule{left:111px;top:3505px;width:978px;height:1px;background:rgba(255,255,255,.7)}
.social{left:591px;top:3529px;display:flex;gap:10px}
.social span{width:16px;height:16px;border-radius:50%;background:var(--white)}
.footer-call{left:517px;top:3580px;width:166px;height:52px;border-radius:28px;background:var(--brand);border:3px solid var(--white);display:flex;align-items:center;gap:10px;padding-left:8px;font-weight:700;font-size:26px}
.footer-call .dot{width:32px;height:32px;border-radius:50%;border:2px solid var(--white);display:flex;align-items:center;justify-content:center}
</style>
</head>
<body>

<section class="hero abs"></section>
<div class="abs hero-band" aria-hidden="true"></div>
<div class="abs zodiac-wheel" role="img" aria-label="Φωτεινός ζωδιακός τροχός με τα δώδεκα ζώδια"></div>

<header class="site-header">
  <div class="abs site-logo">pelikorax</div>
  <nav class="nav">
    <a style="left:495px" href="#">αστρολόγοι</a>
    <a style="left:644px" href="#">πακέτα κλήσεων</a>
    <a style="left:847px" href="#">Blog</a>
  </nav>
  <a class="abs call-pill" style="left:925px;top:44px;width:162px" href="#">
    <span class="icon"><svg width="16" height="16" viewBox="0 0 24 24"><path fill="#6B429C" d="M6.6 10.8a15 15 0 006.6 6.6l2.2-2.2c.3-.3.7-.4 1-.2 1.1.4 2.3.6 3.6.6.6 0 1 .4 1 1V20c0 .6-.4 1-1 1A17 17 0 013 4c0-.6.4-1 1-1h3.5c.6 0 1 .4 1 1 0 1.3.2 2.5.6 3.6.1.3 0 .7-.2 1z"/></svg></span>
    <span><small>κάλεσε τώρα</small><b>14777</b></span>
  </a>
</header>

<h1 class="abs hero-title bold-heading">Καλωσόρισες στο<br>Τα ζώδια για σήμερα</h1>
<p class="abs hero-lead">Το τυπικό κομμάτι του Lorem Ipsum που χρησιμοποιήθηκε από το 1500 αναπαράγεται παρακάτω για όσους ενδιαφέρονται.</p>
<a class="abs call-pill" style="left:113px;top:503px;width:162px" href="#">
  <span class="icon"><svg width="16" height="16" viewBox="0 0 24 24"><path fill="#6B429C" d="M6.6 10.8a15 15 0 006.6 6.6l2.2-2.2c.3-.3.7-.4 1-.2 1.1.4 2.3.6 3.6.6.6 0 1 .4 1 1V20c0 .6-.4 1-1 1A17 17 0 013 4c0-.6.4-1 1-1h3.5c.6 0 1 .4 1 1 0 1.3.2 2.5.6 3.6.1.3 0 .7-.2 1z"/></svg></span>
  <span><small>κάλεσε τώρα</small><b>14777</b></span>
</a>

<section class="astrologers abs"></section>
<h2 class="abs section-title bold-heading" style="top:842px">Οι αστρολόγοι μας</h2>

<div class="abs slide-arrow" style="left:53px;top:1173px"><svg width="12" height="12" viewBox="0 0 12 12"><path d="M10 6H2M5 3L2 6l3 3" stroke="#6B429C" stroke-width="1.8" fill="none"/></svg></div>
<div class="abs slide-arrow" style="left:1095px;top:1173px"><svg width="12" height="12" viewBox="0 0 12 12"><path d="M2 6h8M7 3l3 3-3 3" stroke="#6B429C" stroke-width="1.8" fill="none"/></svg></div>

<article class="abs card astro-card" style="left:94px">
  <div class="astro-photo" role="img" aria-label="Πορτρέτο αστρολόγου σε έναστρο φόντο">
    <div class="astro-name bold-heading">Ελένη<br>Σταυρίδου</div>
    <div class="astro-role bold-heading">Αστρολόγος</div>
    <div class="contact-pill" style="left:36px"><span class="dot"><svg width="18" height="18" viewBox="0 0 24 24"><path fill="#fff" d="M6.6 10.8a15 15 0 006.6 6.6l2.2-2.2c.3-.3.7-.4 1-.2 1.1.4 2.3.6 3.6.6.6 0 1 .4 1 1V20c0 .6-.4 1-1 1A17 17 0 013 4c0-.6.4-1 1-1h3.5c.6 0 1 .4 1 1 0 1.3.2 2.5.6 3.6.1.3 0 .7-.2 1z"/></svg></span>14777</div>
    <div class="contact-pill" style="left:246px"><span class="dot"><svg width="18" height="14" viewBox="0 0 18 14"><rect x="1" y="1" width="16" height="12" rx="1" fill="#fff"/><path d="M1 1l8 6 8-6" stroke="#6B429C" stroke-width="1.5" fill="none"/></svg></span>14777</div>
  </div>
  <p class="astro-text">Αστρολόγος με εξειδίκευση στην Αστροψυχολογία, με πολλά χρόνια έρευνας πάνω στις ανθρώπινες σχέσεις. Κάλεσε τώρα για μια προσωπική αστρολογική πρόβλεψη. Έχω τις απαντήσεις στα ερωτήματα που σε απασχολούν.</p>
  <a class="astro-link" href="#">Επικοινώνησε τώρα</a>
</article>

<article class="abs card astro-card" style="left:598px">
  <div class="astro-photo" style="background:linear-gradient(120deg,#5a6fd0,#4a3aa8 55%,#3a2390)" role="img" aria-label="Πορτρέτο αστρολόγου σε φόντο με αστερισμούς">
    <div class="astro-name bold-heading">Ελένη<br>Σταυρίδου</div>
    <div class="astro-role bold-heading">Αστρολόγος</div>
    <div class="contact-pill" style="left:36px"><span class="dot"><svg width="18" height="18" viewBox="0 0 24 24"><path fill="#fff" d="M6.6 10.8a15 15 0 006.6 6.6l2.2-2.2c.3-.3.7-.4 1-.2 1.1.4 2.3.6 3.6.6.6 0 1 .4 1 1V20c0 .6-.4 1-1 1A17 17 0 013 4c0-.6.4-1 1-1h3.5c.6 0 1 .4 1 1 0 1.3.2 2.5.6 3.6.1.3 0 .7-.2 1z"/></svg></span>14777</div>
    <div class="contact-pill" style="left:246px"><span class="dot"><svg width="18" height="14" viewBox="0 0 18 14"><rect x="1" y="1" width="16" height="12" rx="1" fill="#fff"/><path d="M1 1l8 6 8-6" stroke="#6B429C" stroke-width="1.5" fill="none"/></svg></span>14777</div>
  </div>
  <p class="astro-text">Αστρολόγος με εξειδίκευση στην Αστροψυχολογία, με πολλά χρόνια έρευνας πάνω στις ανθρώπινες σχέσεις. Κάλεσε τώρα για μια προσωπική αστρολογική πρόβλεψη. Έχω τις απαντήσεις στα ερωτήματα που σε απασχολούν.</p>
  <a class="astro-link" href="#">Επικοινώνησε τώρα</a>
</article>

<section class="packages abs"></section>
<h2 class="abs section-title bold-heading" style="top:1713px">τηλεφωνικά πακέτα</h2>

<div class="abs package" style="left:112px"><h3 class="bold-heading">20 λεπτά χρόνο ομιλίας</h3><div class="price">30€</div><p>Το <span>Lorem Ipsum</span> είναι απλώς εικονικό κείμενο της βιομηχανίας εκτύπωσης και</p></div>
<div class="abs package featured" style="left:443px"><h3 class="bold-heading">40 λεπτά χρόνο ομιλίας</h3><div class="price">70€</div><p>Το <span>Lorem Ipsum</span> είναι απλώς εικονικό κείμενο της βιομηχανίας εκτύπωσης και</p></div>
<div class="abs package" style="left:773px"><h3 class="bold-heading">80 λεπτά χρόνο ομιλίας</h3><div class="price">120€</div><p>Το <span>Lorem Ipsum</span> είναι απλώς εικονικό κείμενο της βιομηχανίας εκτύπωσης και</p></div>

<section class="blog abs"></section>
<h2 class="abs section-title bold-heading" style="top:2400px">τηλεφωνικά πακέτα</h2>

<div class="abs post-image" style="left:176px;top:2510px;width:446px;height:234px" role="img" aria-label="Χέρι που απλώνει κάρτες ταρό δίπλα σε κερί"></div>
<article class="abs card post-card" style="left:622px;top:2541px">
  <span class="post-rule"></span>
  <div class="date"><small>22</small><b>Ιαν</b></div>
  <h4>Το Lorem Ipsum είναι απλώς εικονικό</h4>
  <p>Το Lorem Ipsum είναι απλώς εικονικό κείμενο της βιομηχανίας εκτύπωσης και στοιχειοθεσίας. Το Lorem Ipsum ήταν το τυπικό εικονικό κείμενο της βιομηχανίας από το 1500, όταν ένας άγνωστος</p>
</article>

<div class="abs post-image globe" style="left:566px;top:2847px;width:466px;height:235px" role="img" aria-label="Χέρια που κρατούν φωτεινό ζωδιακό κύκλο"></div>
<article class="abs card post-card" style="left:176px;top:2878px">
  <span class="post-rule"></span>
  <div class="date"><small>22</small><b>Ιαν</b></div>
  <h4>Το Lorem Ipsum είναι απλώς εικονικό</h4>
  <p>Το Lorem Ipsum είναι απλώς εικονικό κείμενο της βιομηχανίας εκτύπωσης και στοιχειοθεσίας. Το Lorem Ipsum ήταν το τυπικό εικονικό κείμενο της βιομηχανίας από το 1500, όταν ένας άγνωστος</p>
</article>

<div class="abs slide-arrow" style="left:573px;top:3171px"><svg width="10" height="10" viewBox="0 0 10 10"><path d="M6.5 1.5L3 5l3.5 3.5" stroke="#333" stroke-width="1.8" fill="none"/></svg></div>
<div class="abs slide-arrow" style="left:602px;top:3171px"><svg width="10" height="10" viewBox="0 0 10 10"><path d="M3.5 1.5L7 5 3.5 8.5" stroke="#333" stroke-width="1.8" fill="none"/></svg></div>

<footer class="footer abs"></footer>
<div class="abs footer-logo">pelikorax</div>
<nav class="abs foot-links"><span>αστρολόγοι</span><span>πακέτα κλήσεων</span><span>Τελευταίο Blog</span><span>Επικοινωνήστε μαζί μας</span></nav>
<p class="abs copyright">© Copyright 2022 pelikorax.gr | Όλα τα δικαιώματα διατηρούνται.</p>
<div class="abs rule"></div>
<div class="abs social"><span></span><span></span><span></span></div>
<div class="abs footer-call"><span class="dot"><svg width="16" height="16" viewBox="0 0 24 24"><path fill="#fff" d="M6.6 10.8a15 15 0 006.6 6.6l2.2-2.2c.3-.3.7-.4 1-.2 1.1.4 2.3.6 3.6.6.6 0 1 .4 1 1V20c0 .6-.4 1-1 1A17 17 0 013 4c0-.6.4-1 1-1h3.5c.6 0 1 .4 1 1 0 1.3.2 2.5.6 3.6.1.3 0 .7-.2 1z"/></svg></span>14777</div>

</body>
</html>
```